Legal Service Estimated Retainer and Average Case Value

We need an 11x14 flyer that contains the standard retainers and average cost be case, both provided in documents, for each case type we handle. We need the information displayed, preferably in a way that makes the information readable but less troubling to a client shocked at price of litigation. We need one sheet with the retainers and average case value merged into one table.

Target Market(s)

Potential Clients

Font styles to use
Serif
Sans Serif

```html
<!DOCTYPE html>
<html lang="en">
<head>
<meta charset="UTF-8">
<title>Legal Service Estimated Retainer and Average Case Value</title>
<link rel="stylesheet" href="https://fonts.googleapis.com/css2?family=Merriweather:wght@300;400;700&display=swap">
<style>
  :root {
    --navy-top: #21408c;
    --navy-bottom: #131b48;
    --header-blue: #0453a6;
    --row-alt: #e3eaf6;
    --row-white: #ffffff;
    --divider: #b9cbe8;
    --gold: #fdc45a;
    --gold-light: #fedd95;
    --ink: #141a3a;
    --white: #ffffff;
    --photo-light: #ece8e2;
    --photo-wood: #8a3d1c;
  }
  * { margin: 0; padding: 0; box-sizing: border-box; }
  html, body { width: 990px; height: 1200px; overflow: hidden; background: #f2f2f2; }
  .flyer {
    position: relative;
    width: 990px;
    height: 1200px;
    overflow: hidden;
    background: linear-gradient(180deg, var(--navy-top) 0%, var(--navy-bottom) 100%);
    font-family: "Merriweather", Georgia, serif;
  }
  .flyer-art { position: absolute; inset: 0; }
  .brand-top {
    position: absolute;
    top: 70px;
    right: 55px;
    color: var(--white);
    font-size: 22px;
    font-weight: 400;
    letter-spacing: 0.5px;
  }
  .title {
    position: absolute;
    top: 208px;
    right: 52px;
    text-align: right;
    color: var(--white);
    font-weight: 400;
    font-size: 33px;
    line-height: 45px;
    letter-spacing: 0.3px;
  }
  .fee-table {
    position: absolute;
    top: 326px;
    left: 55px;
    width: 880px;
    border-collapse: collapse;
    table-layout: fixed;
  }
  .fee-table th {
    background: var(--header-blue);
    color: var(--white);
    font-weight: 700;
    font-size: 19px;
    height: 56px;
    letter-spacing: 0.3px;
  }
  .fee-table th.case-col { text-align: left; padding-left: 26px; }
  .fee-table th + th { border-left: 1px solid var(--divider); }
  .fee-table td {
    color: var(--ink);
    height: 48px;
    background: var(--row-white);
  }
  .fee-table tr.tall td { height: 60px; }
  .fee-table tbody tr:nth-child(even) td { background: var(--row-alt); }
  .fee-table td.case-type {
    font-size: 16px;
    font-weight: 400;
    padding-left: 26px;
    line-height: 19px;
  }
  .fee-table td.fee {
    text-align: center;
    font-size: 14px;
    font-weight: 300;
    border-left: 1px solid var(--divider);
  }
  .firm-name {
    position: absolute;
    left: 60px;
    top: 1112px;
    display: flex;
    align-items: center;
    gap: 14px;
    color: var(--header-blue);
    color: #18256a;
    font-weight: 400;
  }
  .firm-mark { width: 46px; height: 46px; background: #18256a; }
  .firm-text { line-height: 1; }
  .firm-text .small { display: block; font-size: 13px; letter-spacing: 0.5px; margin-bottom: 4px; }
  .firm-text .big { display: block; font-size: 26px; letter-spacing: 0.5px; }
  .contact {
    position: absolute;
    left: 612px;
    top: 1098px;
    color: var(--white);
    font-size: 12.5px;
    font-weight: 300;
    list-style: none;
  }
  .contact li { display: flex; align-items: flex-start; gap: 8px; line-height: 19px; margin-bottom: 9px; }
  .contact svg { flex: none; margin-top: 4px; }
</style>
</head>
<body>
<main class="flyer">
  <svg class="flyer-art" width="990" height="1200" viewBox="0 0 990 1200">
    <defs>
      <linearGradient id="photoTone" x1="0" y1="0" x2="1" y2="1">
        <stop offset="0" stop-color="#f1eee9"/>
        <stop offset="0.5" stop-color="#e6ded4"/>
        <stop offset="1" stop-color="#d8cfc4"/>
      </linearGradient>
      <radialGradient id="woodTone" cx="0.28" cy="0.28" r="0.25">
        <stop offset="0" stop-color="#9a4a22" stop-opacity="0.75"/>
        <stop offset="1" stop-color="#9a4a22" stop-opacity="0"/>
      </radialGradient>
    </defs>
    <!-- header image area -->
    <g role="img" aria-label="Photo of a wooden judge's gavel resting on its sound block">
      <path d="M0,0 H560 C400,70 250,170 170,300 C140,230 85,185 0,170 Z" fill="url(#photoTone)"/>
      <path d="M0,0 H560 C400,70 250,170 170,300 C140,230 85,185 0,170 Z" fill="url(#woodTone)"/>
    </g>
    <!-- gold curves -->
    <path d="M0,150 C90,165 150,210 170,300 C140,230 85,185 0,170 Z" fill="var(--gold)"/>
    <path d="M0,160 C85,172 140,210 168,290" fill="none" stroke="var(--gold-light)" stroke-width="3"/>
    <path d="M520,0 H680 C470,60 270,160 170,300 C250,170 380,70 520,0 Z" fill="var(--gold)"/>
    <path d="M600,0 C420,60 260,170 172,296" fill="none" stroke="var(--gold-light)" stroke-width="4"/>
    <!-- footer -->
    <path d="M0,1040 C20,1075 60,1090 120,1092 H460 C540,1092 590,1140 605,1200 H0 Z" fill="var(--gold)"/>
    <path d="M0,1058 C25,1090 70,1100 125,1100 H455 C530,1100 575,1150 588,1200 H0 Z" fill="var(--white)"/>
  </svg>

  <div class="brand-top">Whitfield Law</div>

  <h1 class="title">Legal Service Estimated<br>Retainer and Average Case Value</h1>

  <table class="fee-table">
    <colgroup>
      <col style="width:419px"><col style="width:222px"><col style="width:239px">
    </colgroup>
    <thead>
      <tr><th class="case-col">Case Type</th><th>Retainer Fee</th><th>Average Fee</th></tr>
    </thead>
    <tbody>
      <tr><td class="case-type">Divorce (3301 C)</td><td class="fee">$2,000</td><td class="fee">$1,500 - $3,000</td></tr>
      <tr><td class="case-type">Divorce (3301 D)</td><td class="fee">$2,500</td><td class="fee">$2,000 - $3,000</td></tr>
      <tr><td class="case-type">Divorce and Custody</td><td class="fee">$3,500</td><td class="fee">$5,000 - $8,000</td></tr>
      <tr><td class="case-type">Divorce and Equitable Distribution</td><td class="fee">$3,500</td><td class="fee">$6,000 - $10,000</td></tr>
      <tr><td class="case-type">Divorce and Support</td><td class="fee">$3,000</td><td class="fee">$2,000 - $4,000</td></tr>
      <tr><td class="case-type">Divorce, Custody and Support</td><td class="fee">$3,500</td><td class="fee">$8,000 - $12,000</td></tr>
      <tr class="tall"><td class="case-type">Divorce, Equitable Distribution<br>and Support</td><td class="fee">$3,500</td><td class="fee">$8,000 - $12,000</td></tr>
      <tr class="tall"><td class="case-type">Divorce, Equitable Distribution<br>and Custody</td><td class="fee">$5,000</td><td class="fee">$10,000 - $15,000</td></tr>
      <tr class="tall"><td class="case-type">Divorce, Equitable Distribution,<br>Custody and Support</td><td class="fee">$3,500</td><td class="fee">$12,000 - $15,000</td></tr>
      <tr><td class="case-type">Custody Initial Order</td><td class="fee">$3,000</td><td class="fee">$4,000 - $7,000</td></tr>
      <tr><td class="case-type">Divorce, Custody and Support</td><td class="fee">$3,500</td><td class="fee">$5,000 - $8,000</td></tr>
      <tr><td class="case-type">Custody and Support</td><td class="fee">$3,000</td><td class="fee">$5,000 - $8,000</td></tr>
      <tr><td class="case-type">(PFA) Protection From Abuse</td><td class="fee">$2,000 Paid In Full</td><td class="fee">$1,500 - $3,000</td></tr>
    </tbody>
  </table>

  <div class="firm-name">
    <span class="firm-mark" aria-hidden="true"></span>
    <span class="firm-text"><span class="small">THE LAW OFFICE OF</span><span class="big">DANIEL M WHITFIELD</span></span>
  </div>

  <ul class="contact">
    <li>
      <svg width="11" height="11" viewBox="0 0 24 24" aria-hidden="true"><path fill="var(--gold)" d="M6.6 10.8a15.1 15.1 0 0 0 6.6 6.6l2.2-2.2a1 1 0 0 1 1-.25 11.4 11.4 0 0 0 3.6.57 1 1 0 0 1 1 1V20a1 1 0 0 1-1 1A17 17 0 0 1 3 4a1 1 0 0 1 1-1h3.5a1 1 0 0 1 1 1c0 1.25.2 2.45.57 3.57a1 1 0 0 1-.25 1z"/></svg>
      (555) 214-0376
    </li>
    <li>
      <svg width="11" height="12" viewBox="0 0 24 24" aria-hidden="true"><path fill="var(--gold)" d="M12 2a7 7 0 0 0-7 7c0 5.2 7 13 7 13s7-7.8 7-13a7 7 0 0 0-7-7zm0 9.5A2.5 2.5 0 1 1 12 6.5a2.5 2.5 0 0 1 0 5z"/></svg>
      <span>2150 Ridgeview Avenue<br>Suite 210, Maplewood, PA 17000</span>
    </li>
    <li>
      <svg width="11" height="11" viewBox="0 0 24 24" aria-hidden="true"><g fill="none" stroke="var(--gold)" stroke-width="2"><circle cx="12" cy="12" r="10"/><path d="M2 12h20M12 2c3 3 3 17 0 20M12 2c-3 3-3 17 0 20"/></g></svg>
      www.whitfieldlawoffice.com
    </li>
  </ul>
</main>
</body>
</html>
```